Audit/Compliance company needs Business Card Template

We are after a Business Card Template that we can modify internally to update details as people change positions.
We are an Australian based company specalising in Auditing and Quality/OHS systems development. - See www.keelbrookmeridian.com.au for more information
We would like the desings to be based around our logo and colours assocaited with it (attached for your information) however we are very open as to how the cards are designed.
We are looking for something quite edgy and mordern but it must have a professional/compliance feel to it (if possible).
The main details we would like to include within the card template are:
Name
Position Title
Postal Address
Phone Number
Mobile Number
Email Address
Website
The cards will be printed through folio mint on Glossy paper so it should reflect the requirements below
Full Bleed Size (starting document size)
90 x 52 mm
1062 x 615 pixels
Document Trim Size (final size after being cut)
87 x 49 mm
1028 x 579 pixels
Resolution
300 DPI

```html
<!DOCTYPE html>
<html lang="en">
<head>
<meta charset="utf-8">
<title>Keelbrook Meridian – Business Card</title>
<link href="https://fonts.googleapis.com/css2?family=Open+Sans:wght@300;400;600;700&display=swap" rel="stylesheet">
<style>
  :root {
    --card-bg: #ffffff;
    --ink-dark: #3b3b3b;
    --ink-mid: #555555;
    --ink-soft: #6a6a6a;
    --accent: #f26522;
    --decor-light: #ececec;
    --decor-mid: #dcdcdc;
  }
  html, body {
    margin: 0;
    padding: 0;
    width: 1200px;
    height: 676px;
    overflow: hidden;
    background: var(--card-bg);
  }
  .card {
    position: relative;
    width: 1200px;
    height: 676px;
    background: var(--card-bg);
    font-family: "Open Sans", sans-serif;
    color: var(--ink-dark);
    overflow: hidden;
  }
  .brand-decor {
    position: absolute;
    left: 630px;
    top: 0;
    width: 570px;
    height: 500px;
    background: radial-gradient(ellipse at 55% 40%, var(--decor-mid) 0%, var(--decor-light) 45%, rgba(255,255,255,0) 72%);
  }
  .brand {
    position: absolute;
    left: 26px;
    top: 148px;
    display: flex;
    align-items: center;
    gap: 20px;
  }
  .brand-mark {
    width: 54px;
    height: 54px;
    background: var(--accent);
  }
  .brand-name {
    font-size: 36px;
    font-weight: 600;
    letter-spacing: 1px;
    color: var(--ink-dark);
    text-transform: uppercase;
  }
  .person {
    position: absolute;
    left: 23px;
    top: 448px;
    width: 246px;
  }
  .person-name {
    margin: 0;
    font-size: 30px;
    font-weight: 700;
    color: var(--ink-dark);
    line-height: 1.2;
  }
  .person-position {
    margin: 8px 0 0;
    text-align: right;
    font-size: 25px;
    font-weight: 300;
    color: var(--ink-mid);
  }
  .divider {
    position: absolute;
    left: 334px;
    top: 457px;
    width: 2px;
    height: 74px;
    background: var(--accent);
  }
  .contact {
    position: absolute;
    margin: 0;
    padding: 0;
    list-style: none;
    font-size: 22px;
    color: var(--ink-mid);
  }
  .contact li {
    display: flex;
    align-items: center;
    height: 40px;
  }
  .contact svg {
    width: 24px;
    height: 24px;
    margin-right: 8px;
    flex: none;
  }
  .contact-phones { left: 348px; top: 455px; }
  .contact-online { left: 606px; top: 449px; }
  .contact-online svg { margin-right: 14px; }
  .address {
    position: absolute;
    left: 355px;
    top: 550px;
    margin: 0;
    font-style: normal;
    font-size: 22px;
    line-height: 35px;
    color: var(--ink-mid);
  }
  .address-company { color: var(--accent); display: block; }
</style>
</head>
<body>
<main class="card">
  <div class="brand-decor" role="img" aria-label="Faint brand decoration area"></div>

  <div class="brand">
    <span class="brand-mark"></span>
    <span class="brand-name">Keelbrook Meridian</span>
  </div>

  <section class="person">
    <h1 class="person-name">Name Surname</h1>
    <p class="person-position">Position</p>
  </section>

  <span class="divider"></span>

  <ul class="contact contact-phones">
    <li>
      <svg viewBox="0 0 24 24" aria-hidden="true"><path fill="var(--accent)" d="M6.6 10.8a15.2 15.2 0 0 0 6.6 6.6l2.2-2.2c.3-.3.7-.4 1-.2 1.1.4 2.3.6 3.6.6.6 0 1 .4 1 1V20c0 .6-.4 1-1 1A17 17 0 0 1 3 4c0-.6.4-1 1-1h3.5c.6 0 1 .4 1 1 0 1.3.2 2.5.6 3.6.1.3 0 .7-.2 1z"/></svg>
      <span>1300 555 214</span>
    </li>
    <li>
      <svg viewBox="0 0 24 24" aria-hidden="true"><rect x="6" y="2" width="12" height="20" rx="2" fill="none" stroke="var(--accent)" stroke-width="2"/><circle cx="12" cy="18" r="1.2" fill="var(--accent)"/></svg>
      <span>1300 555 214</span>
    </li>
  </ul>

  <ul class="contact contact-online">
    <li>
      <svg viewBox="0 0 24 24" aria-hidden="true"><circle cx="12" cy="12" r="9" fill="none" stroke="var(--accent)" stroke-width="2"/><path d="M3 12h18M12 3c3 3 3 15 0 18M12 3c-3 3-3 15 0 18" fill="none" stroke="var(--accent)" stroke-width="1.6"/></svg>
      <span>www.keelbrookmeridian.com.au</span>
    </li>
    <li>
      <svg viewBox="0 0 24 24" aria-hidden="true"><rect x="2" y="6" width="20" height="14" rx="1" fill="none" stroke="var(--accent)" stroke-width="2"/><path d="M2 7l10 7 10-7" fill="none" stroke="var(--accent)" stroke-width="2"/></svg>
      <span>email.address@keelbrook-meridian.com.au</span>
    </li>
  </ul>

  <address class="address">
    <span class="address-company">Keelbrook Meridian</span>
    Road 9th Suite 12, Sydney, Australia
  </address>
</main>
</body>
</html>
```